Buisness card

**Front Side:**

**[Your Company Logo]**
**Steadfast Upkeep Industrial**
*Keeping Your Equipment Running Smoothly*

**Contact Information:**
- **Name:** [darren Whitlow
- **Title:** [owner
- **Phone:** [8025196047
- **Email:** darren@sukrn.com

**Back Side:**

**Services Offered:**
- Routine Inspections
- Equipment Maintenance
- Emergency Repairs
- Consultation Services
- New installs
Tag line
Be proactive not reactive

```html
<!DOCTYPE html>
<html lang="en">
<head>
<meta charset="utf-8">
<title>Steadfast Upkeep Industrial – Business Card</title>
<link href="https://fonts.googleapis.com/css2?family=Montserrat:wght@300;400;500;600;700;800&display=swap" rel="stylesheet">
<style>
  :root {
    --navy: #1f2e6b;
    --navy-emboss: #263878;
    --blue: #3a62c0;
    --blue-tab: #3d68c4;
    --cyan: #2ec5f2;
    --white: #ffffff;
    --ink-soft: #4a4f60;
    --stage: #e9eaec;
  }
  * { box-sizing: border-box; margin: 0; padding: 0; }
  html, body {
    width: 1200px; height: 802px; overflow: hidden;
    background: var(--stage);
    font-family: "Montserrat", sans-serif;
  }
  .sheet {
    width: 1200px; height: 802px;
    display: flex; align-items: center; justify-content: center; gap: 40px;
  }
  .card {
    position: relative; width: 540px; height: 310px;
    border-radius: 22px; overflow: hidden;
    box-shadow: 0 10px 30px rgba(0,0,0,.18);
  }
  .card svg.band { position: absolute; left: 0; bottom: 0; }

  /* Front */
  .card--front { background: var(--white); }
  .brand {
    position: absolute; top: 34px; right: 40px;
    display: flex; align-items: center; gap: 12px;
  }
  .brand__mark { width: 38px; height: 38px; border-radius: 50%; background: var(--navy); }
  .brand__name {
    font-weight: 700; font-size: 17px; color: var(--navy); line-height: 1.15; width: 150px;
  }
  .person { position: absolute; left: 32px; top: 118px; }
  .person__name { font-size: 30px; font-weight: 700; color: var(--navy); letter-spacing: .2px; line-height: 1.2; }
  .person__name span { color: var(--blue); }
  .person__title { font-size: 17px; font-weight: 300; color: var(--ink-soft); margin-top: 2px; }
  .divider {
    position: absolute; left: 30px; top: 194px; width: 470px; height: 1.5px;
    background: var(--blue); opacity: .8;
  }
  .contacts { position: absolute; left: 36px; top: 203px; list-style: none; }
  .contacts li {
    display: flex; align-items: center; gap: 8px;
    font-size: 14px; color: var(--navy); line-height: 19px;
  }
  .contacts svg { width: 11px; height: 11px; flex: none; }
  .front-tab-text {
    position: absolute; right: 24px; top: 256px;
    font-size: 11.5px; line-height: 16px; font-weight: 500; color: var(--white);
    white-space: nowrap;
  }
  .front-slogan {
    position: absolute; left: 28px; top: 284px;
    font-size: 12.5px; line-height: 18px; font-weight: 500; color: var(--white); letter-spacing: .2px;
  }

  /* Back */
  .card--back { background: var(--navy); }
  .emboss {
    position: absolute; top: 58px; left: 0; right: 0;
    display: flex; align-items: center; justify-content: center; gap: 14px;
  }
  .emboss__mark { width: 60px; height: 60px; border-radius: 50%; background: var(--navy-emboss); }
  .emboss__name {
    font-size: 26px; font-weight: 800; color: var(--navy-emboss); line-height: 1.05; width: 250px;
  }
  .services-label {
    position: absolute; top: 150px; left: 50%; transform: translateX(-50%);
    border: 1.5px solid var(--cyan); border-radius: 20px;
    padding: 4px 16px; font-size: 14px; font-weight: 700; color: var(--white);
    letter-spacing: .4px; white-space: nowrap;
  }
  .services {
    position: absolute; top: 192px; left: 0; right: 0;
    text-align: center; color: var(--white); font-size: 14px; line-height: 22px; font-weight: 400;
  }
  .services .dot { color: var(--cyan); margin: 0 6px; font-weight: 700; }
  .back-tagline {
    position: absolute; left: 140px; top: 276px;
    font-size: 15px; line-height: 20px; font-weight: 500; color: var(--white); letter-spacing: .3px;
  }
</style>
</head>
<body>
<main class="sheet">

  <section class="card card--front" aria-label="Business card front">
    <div class="brand">
      <div class="brand__mark"></div>
      <div class="brand__name">Steadfast Upkeep Industrial</div>
    </div>

    <div class="person">
      <p class="person__name">Darren <span>Whitlow</span></p>
      <p class="person__title">Owner</p>
    </div>
    <div class="divider"></div>

    <ul class="contacts">
      <li>
        <svg viewBox="0 0 12 12"><path d="M3 1l2 2.5-1.2 1.2a7 7 0 003.5 3.5L8.5 7 11 9l-1.3 1.8C5.5 11 1 6.5 1.2 2.3z" fill="#2ec5f2"/></svg>
        8025196047
      </li>
      <li>
        <svg viewBox="0 0 12 12"><rect x="1" y="2.5" width="10" height="7" rx="1" fill="#2ec5f2"/><path d="M1.5 3l4.5 3.5L10.5 3" stroke="#fff" stroke-width="1" fill="none"/></svg>
        darren@sukrn.com
      </li>
      <li>
        <svg viewBox="0 0 12 12"><circle cx="6" cy="6" r="5" fill="#2ec5f2"/><path d="M1 6h10M6 1c2 2 2 8 0 10M6 1c-2 2-2 8 0 10" stroke="#fff" stroke-width=".8" fill="none"/></svg>
        www.sukrn.com
      </li>
    </ul>

    <svg class="band" width="540" height="70" viewBox="0 0 540 70">
      <path d="M300 36 C318 36 318 12 336 12 H540 V36 Z" fill="var(--blue-tab)"/>
      <path d="M0 36 H540 V70 H0 Z" fill="var(--navy)"/>
    </svg>
    <p class="front-tab-text">Steadfast Upkeep Industrial</p>
    <p class="front-slogan">Keeping Your Equipment Running Smoothly</p>
  </section>

  <section class="card card--back" aria-label="Business card back">
    <div class="emboss">
      <div class="emboss__mark"></div>
      <div class="emboss__name">Steadfast Upkeep Industrial</div>
    </div>

    <p class="services-label">SERVICES OFFERED</p>
    <p class="services">
      Routine Inspections<span class="dot">•</span>Equipment Maintenance<span class="dot">•</span>Emergency Repairs<br>
      Consultation Services<span class="dot">•</span>New installs
    </p>

    <svg class="band" width="540" height="60" viewBox="0 0 540 60">
      <path d="M0 58 C60 52 90 50 110 40 C125 22 135 18 160 18 H330 C350 18 352 30 372 30 H540 V60 H0 Z" fill="var(--cyan)"/>
    </svg>
    <p class="back-tagline">Be proactive not reactive</p>
  </section>

</main>
</body>
</html>
```